Roofing Contractor business card redesign

I want to redesign my business card with a fresh, eye catching concept

Target Market(s)

Residential Roofing Clients, potential employees, and subcontractors.

Industry/Entity Type

Business

Colors

Designer to choose colors to be used in the design.

Requirements
Nice to have
• I just want something that's more pleasing to the eye. You can use a combination of either / or of my logos.

```html
<!DOCTYPE html>
<html lang="en">
<head>
<meta charset="utf-8">
<title>Bright Ridge General Contractors – Business Card</title>
<link rel="stylesheet" href="https://fonts.googleapis.com/css2?family=Oswald:wght@500;600&family=Signika:wght@400&family=Open+Sans:wght@700&display=swap">
<style>
  :root {
    --backdrop: #2e2e2e;
    --orange-light: #f5bb3a;
    --orange-mid: #f2a530;
    --orange-deep: #e66f26;
    --accent-yellow: #ffd21f;
    --ink: #4a1a12;
    --text-dark: #3b1a12;
    --card-white: #f5f5f5;
    --emblem-brown: #3e2220;
    --emblem-orange: #e8742a;
  }
  * { margin: 0; padding: 0; box-sizing: border-box; }
  html, body { width: 1200px; height: 960px; overflow: hidden; }
  body { background: var(--backdrop); position: relative; }

  .card {
    position: absolute;
    width: 600px;
    height: 342px;
    overflow: hidden;
  }

  /* Front */
  .card-front {
    left: 320px; top: 103px;
    background: radial-gradient(ellipse at 35% 45%, var(--orange-light) 0%, var(--orange-mid) 40%, var(--orange-deep) 90%);
  }
  .accent-bar {
    position: absolute; left: 0; top: 60px;
    width: 8px; height: 62px;
    background: var(--accent-yellow);
  }
  .contact {
    position: absolute; left: 35px; top: 58px;
    color: var(--text-dark);
    font-family: "Signika", sans-serif;
    font-size: 14.5px;
    line-height: 18px;
  }
  .contact-name {
    font-family: "Oswald", sans-serif;
    font-weight: 500;
    font-size: 27px;
    line-height: 30px;
    letter-spacing: 0.3px;
    text-transform: uppercase;
    color: var(--ink);
  }
  .contact-address { margin-top: 14px; }
  .contact-lines { margin-top: 14px; }

  .crew-emblem {
    position: absolute; left: 262px; top: 12px;
    width: 322px; height: 322px;
  }

  /* Back */
  .card-back {
    left: 317px; top: 488px;
    background: linear-gradient(160deg, #fafafa 0%, var(--card-white) 55%, #ececec 100%);
  }
  .brand {
    position: absolute; left: 0; right: 0; top: 96px;
    display: flex; align-items: center; justify-content: center; gap: 12px;
  }
  .brand-mark {
    width: 78px; height: 78px; border-radius: 50%;
    background: var(--emblem-brown);
    flex: none;
  }
  .brand-name {
    font-family: "Oswald", sans-serif;
    font-weight: 600;
    font-size: 62px;
    line-height: 1;
    color: var(--ink);
    letter-spacing: -0.5px;
  }
  .brand-tagline {
    position: absolute; left: 0; right: 0; top: 197px;
    text-align: center;
    font-family: "Open Sans", sans-serif;
    font-weight: 700;
    font-size: 27px;
    letter-spacing: -0.3px;
    color: var(--ink);
  }
  .social-row {
    position: absolute; left: 150px; top: 282px;
    width: 300px; height: 30px;
  }
</style>
</head>
<body>

  <section class="card card-front" aria-label="Business card front">
    <div class="accent-bar"></div>
    <div class="contact">
      <div class="contact-name">Sam Holloway</div>
      <div class="contact-title">Apex Certified Roof Inspector<br>Licensed Property Adjuster</div>
      <div class="contact-address">4810 Cedar Ridge Drive<br>Suite 118<br>Plano, TX 75024</div>
      <div class="contact-lines">Office: (555) 218-4400<br>Mobile/Text: (555) 364-7120<br>sam@brightridgetx.com<br>www.brightridgetx.com</div>
    </div>
    <svg class="crew-emblem" viewBox="0 0 322 322" role="img" aria-label="Circular emblem illustration of three roofing contractors with tools in front of a house roof">
      <defs>
        <radialGradient id="emblemFill" cx="50%" cy="45%" r="55%">
          <stop offset="0%" stop-color="#e0823a"/>
          <stop offset="60%" stop-color="#8a4a2a"/>
          <stop offset="100%" stop-color="#3e2220"/>
        </radialGradient>
      </defs>
      <circle cx="161" cy="161" r="158" fill="#ffffff"/>
      <circle cx="161" cy="161" r="150" fill="url(#emblemFill)"/>
    </svg>
  </section>

  <section class="card card-back" aria-label="Business card back">
    <div class="brand">
      <span class="brand-name">Bright Ridge</span>
      <span class="brand-mark"></span>
    </div>
    <div class="brand-tagline">General Contractors, Inc.</div>
    <svg class="social-row" viewBox="0 0 300 30" aria-label="Social media links">
      <line x1="0" y1="15" x2="68" y2="15" stroke="#4a1a12" stroke-width="1"/>
      <line x1="232" y1="15" x2="300" y2="15" stroke="#4a1a12" stroke-width="1"/>
      <g fill="none" stroke="#4a1a12" stroke-width="1.6">
        <circle cx="86" cy="15" r="13"/>
        <circle cx="118" cy="15" r="13"/>
        <circle cx="150" cy="15" r="13"/>
        <circle cx="182" cy="15" r="13"/>
        <circle cx="214" cy="15" r="13"/>
      </g>
    </svg>
  </section>

</body>
</html>
```